VaultMeridan Business Card Re-Design

VaultMeridan is a specialized information security company that applies its proven methodology of security Assessment, Development, Integration and Training (A-D-I-T) to provide cyber security services in the areas of Data Protection, Network Defense and Compliance. We need the current business card re-designed to properly scale the fonts and possibly rearranging some elements (icons, lettering, etc.) to make the card more appealing to the eye. The card should have the logo that is on the web site (www.vaultmeridan-example.com). We would like ideas for both a black card (black background) and a white card (white background). We prefer rounded corners to help the card stand out but are open to all ideas. FYI: VaultMeridan's slogan is "...your security is our business".

Target Market(s)

#1 US Government Contracting Companies, #2 Commercial Companies, #3 Gen. Public.

Industry/Entity Type

Business

Contact Information for Business Card

See Description; open to the use of different fonts.

Font styles to use
Sans Serif

Colors
000000
ec1f27
ffffff

Requirements
Must have
• Company logo on web site, rounded corners, list of company offerings on the back of the card.
Nice to have
• Icons
Should not have
• none

```html
<!DOCTYPE html>
<html lang="en">
<head>
<meta charset="utf-8">
<title>VaultMeridan Business Card – Back</title>
<link href="https://fonts.googleapis.com/css2?family=Questrial&display=swap" rel="stylesheet">
<style>
  :root {
    --page-bg: #ffffff;
    --card-bg: #000000;
    --accent-red: #ec1f27;
    --text-white: #ffffff;
    --text-grey: #bdbdbd;
    --card-shadow: rgba(0, 0, 0, 0.45);
  }
  html, body {
    margin: 0;
    padding: 0;
    width: 1200px;
    height: 900px;
    overflow: hidden;
    background: var(--page-bg);
  }
  .canvas {
    position: relative;
    width: 1200px;
    height: 900px;
    font-family: "Questrial", "Century Gothic", sans-serif;
  }
  .business-card {
    position: absolute;
    left: 113px;
    top: 171px;
    width: 960px;
    height: 549px;
    background: var(--card-bg);
    border-radius: 34px;
    box-shadow: 6px 7px 6px var(--card-shadow);
    color: var(--text-white);
  }
  .offerings {
    list-style: none;
    margin: 0;
    padding: 0;
    position: absolute;
    left: 58px;
    top: 52px;
  }
  .offerings li {
    position: relative;
    padding-left: 19px;
    font-size: 23px;
    line-height: 35.5px;
    letter-spacing: 0.6px;
    white-space: nowrap;
  }
  .offerings li::before {
    content: "";
    position: absolute;
    left: 0;
    top: 15px;
    width: 9px;
    height: 9px;
    background: var(--accent-red);
  }
  .offerings .slash {
    color: var(--accent-red);
  }
  .website {
    position: absolute;
    left: 57px;
    top: 467px;
    font-size: 25px;
    letter-spacing: 0.5px;
    color: var(--accent-red);
  }
  .brand {
    position: absolute;
    left: 535px;
    top: 400px;
    display: flex;
    flex-direction: column;
    align-items: flex-start;
  }
  .brand-row {
    display: flex;
    align-items: center;
    gap: 16px;
  }
  .brand-mark {
    width: 26px;
    height: 26px;
    background: var(--accent-red);
  }
  .brand-name {
    font-size: 44px;
    letter-spacing: 6px;
    color: var(--text-white);
    line-height: 1;
  }
  .brand-tagline {
    margin-top: 14px;
    margin-left: 42px;
    font-size: 19px;
    letter-spacing: 1.5px;
    color: var(--text-grey);
    text-transform: uppercase;
  }
</style>
</head>
<body>
<div class="canvas">
  <section class="business-card" aria-label="VaultMeridan business card, back side">
    <ul class="offerings">
      <li>Network Attack Penetration &amp; Defense</li>
      <li>Red<span class="slash">/</span>Blue Team</li>
      <li>Data Center Consolidation</li>
      <li>Secure Virtual Computing</li>
      <li>Classified Cross Domain Solutions</li>
      <li>Foreign<span class="slash">/</span>Counter Intelligence Data Security</li>
      <li>Certification &amp; Accreditation</li>
      <li>Secure Wireless Solutions</li>
      <li>Security Training, Assessment &amp; Integration</li>
      <li>Executive Security Strategy Coaching</li>
      <li>Data Encryption<span class="slash">/</span>Privacy</li>
    </ul>
    <div class="website">www.vaultmeridan-example.com</div>
    <div class="brand">
      <div class="brand-row">
        <span class="brand-mark" aria-hidden="true"></span>
        <span class="brand-name">VaultMeridan</span>
      </div>
      <div class="brand-tagline">Information Security</div>
    </div>
  </section>
</div>
</body>
</html>
```